Company's name is: Merry Harvest Foods, Inc.; Product is: Smoked Chicken

Need a high quality, attractive, colorful label that will be used on our smoked chicken packaging. Our packaging consists of a regular plastic tray for whole chicken, with a clear bumpy cover that snaps over the tray. The label will be placed on top of the clear cover.
We are looking for a unique label. This could feature a nice picture of a whole golden brown smoked chicken, the company's name and address (or its initials MHF) nicely scripted, the nutrition panel, the name of the product it contains "Smoked Chicken - Cooked", weight, etc.
Please note that smoked chicken will be distributed to supermarkets, restaurants and health food stores.
We are thinking that the label should include nice colors (maybe a mixture of blue, red, golden brown, etc?) that will make our product catchy to the eyes and stand out on the shelves. We will have 2 varieties of smoked chicken: Fresh AND Organic.

Target Market(s)

Supermarkets
Wholesale delivery to restaurants
Valmart
TK's

Industry/Entity Type

It Company

Font styles to use
Decorative
Script

Requirements
Must have
• A nice picture of golden brown smoked chicken.
• Creative colors (~3) on the label
• Different sizes and fonts
• the company's name and address (or its initials MHF) nicely scripted, the nutrition panel, the name of the product it contains "Smoked Chicken - Cooked", weight, etc.
Nice to have
• There are some nice labels on Smoked chicken sold in Europe (France, Germany, etc). We suggest using Searchly to see some for inspiration if necessary.
Should not have
• My project must not be crowded with writings. A clean, attractive and professionally designed label is what we are looking for.
• Picture of the whole smoked chicken should be as natural looking as possible.

```html
<!DOCTYPE html>
<html lang="en">
<head>
<meta charset="utf-8">
<title>Merry Harvest Foods – Smoked Chicken Label</title>
<link href="https://fonts.googleapis.com/css2?family=Arimo:wght@400;700&family=Roboto+Condensed:wght@400;700&family=Tinos:wght@700&display=swap" rel="stylesheet">
<style>
  :root {
    --page-bg: #fefbd0;
    --deep-red: #9a2112;
    --rust: #b8460f;
    --amber: #d98a10;
    --gold: #e8b614;
    --brand-gold: #e0982a;
    --royal-blue: #2b2a87;
    --sun-yellow: #f6e400;
    --white: #ffffff;
    --ink: #111111;
    --eco-green: #3a9a3a;
  }
  html, body {
    margin: 0;
    padding: 0;
    width: 1200px;
    height: 1200px;
    overflow: hidden;
    background: var(--page-bg);
  }
  .label-canvas {
    display: block;
    width: 1200px;
    height: 1200px;
  }
  .brand-initials { font-family: "Arimo", sans-serif; font-weight: 700; fill: var(--brand-gold); }
  .product-title { font-family: "Arimo", sans-serif; font-weight: 700; fill: var(--white); }
  .cooked-tag-text { font-family: "Arimo", sans-serif; font-weight: 700; fill: var(--white); }
  .company-name { font-family: "Roboto Condensed", sans-serif; font-weight: 700; fill: var(--white); }
  .contact-line { font-family: "Roboto Condensed", sans-serif; font-weight: 400; fill: var(--white); }
  .net-weight { font-family: "Tinos", serif; font-weight: 700; fill: var(--white); }
  .nutrition-title { font-family: "Arimo", sans-serif; font-weight: 700; fill: var(--ink); }
  .nutrition-row { font-family: "Arimo", sans-serif; fill: var(--ink); }
  .nutrition-row.bold { font-weight: 700; }
</style>
</head>
<body>
<svg class="label-canvas" viewBox="0 0 1200 1200" xmlns="http://www.w3.org/2000/svg">
  <defs>
    <radialGradient id="warmGlow" cx="600" cy="680" r="340" gradientUnits="userSpaceOnUse">
      <stop offset="0" stop-color="var(--gold)"/>
      <stop offset="0.35" stop-color="var(--amber)"/>
      <stop offset="0.7" stop-color="var(--rust)"/>
      <stop offset="1" stop-color="var(--deep-red)"/>
    </radialGradient>
    <radialGradient id="chickenTones" cx="0.5" cy="0.45" r="0.6">
      <stop offset="0" stop-color="#c8752e"/>
      <stop offset="0.6" stop-color="#9a4a1c"/>
      <stop offset="1" stop-color="#6a2e12"/>
    </radialGradient>
    <linearGradient id="stripeFade" x1="600" y1="0" x2="848" y2="0" gradientUnits="userSpaceOnUse">
      <stop offset="0" stop-color="var(--sun-yellow)" stop-opacity="0"/>
      <stop offset="0.4" stop-color="var(--sun-yellow)"/>
      <stop offset="1" stop-color="var(--sun-yellow)"/>
    </linearGradient>
    <clipPath id="labelShape">
      <path d="M324,392 Q600,116 876,392 Q838,600 876,808 Q600,1084 324,808 Q362,600 324,392 Z"/>
    </clipPath>
  </defs>

  <g class="label" clip-path="url(#labelShape)">
    <rect class="label-background" x="300" y="240" width="600" height="720" fill="url(#warmGlow)"/>

    <path class="product-photo" role="img" aria-label="Photo of a whole golden brown smoked chicken on lettuce with tomato and lemon wedges"
          d="M356,772 Q372,700 440,660 Q520,612 600,590 Q680,548 744,552 Q790,580 800,660 L806,700 Q720,770 600,786 Q470,800 356,790 Z"
          fill="url(#chickenTones)"/>

    <path class="accent-stripe" d="M600,796 Q760,740 848,640 L856,668 Q740,780 600,800 Z" fill="url(#stripeFade)"/>
    <path class="base-band" d="M300,802 Q650,796 852,656 L900,656 L900,960 L300,960 Z" fill="var(--royal-blue)"/>
  </g>

  <text class="brand-initials" x="600" y="350" text-anchor="middle" font-size="54">MHF</text>

  <text class="product-title" x="600" y="458" text-anchor="middle" font-size="68">SMOKED</text>
  <text class="product-title" x="600" y="522" text-anchor="middle" font-size="60">Chicken</text>

  <g class="cooked-tag" transform="translate(428,598) rotate(-24)">
    <rect x="-90" y="-24" width="180" height="48" fill="var(--royal-blue)"/>
    <text class="cooked-tag-text" x="-6" y="12" text-anchor="middle" font-size="34">Cooked</text>
  </g>

  <text class="company-name" x="402" y="836" font-size="19">Merry Harvest Foods, Inc</text>
  <text class="contact-line" x="472" y="859" font-size="11">14 Orchard Lane , Suite 02</text>
  <text class="contact-line" x="472" y="873" font-size="11">T 0555 014 223</text>
  <text class="contact-line" x="472" y="887" font-size="11">e hello@merryharvest.com</text>

  <g class="nutrition-panel">
    <rect x="606" y="811" width="92" height="93" rx="4" fill="var(--white)"/>
    <rect x="609" y="814" width="86" height="87" rx="2" fill="none" stroke="var(--ink)" stroke-width="1.4"/>
    <text class="nutrition-title" x="613" y="826" font-size="9">Nutrition Facts</text>
    <text class="nutrition-row" x="613" y="832" font-size="3">Serving Size 3oz (84g)</text>
    <line x1="612" y1="834" x2="692" y2="834" stroke="var(--ink)" stroke-width="2"/>
    <text class="nutrition-row" x="613" y="839" font-size="3">Amount Per Serving</text>
    <text class="nutrition-row bold" x="613" y="843" font-size="3">Calories 160</text>
    <line x1="612" y1="845" x2="692" y2="845" stroke="var(--ink)" stroke-width="1"/>
    <text class="nutrition-row bold" x="691" y="849" font-size="3" text-anchor="end">% Daily Value</text>
    <text class="nutrition-row bold" x="613" y="853" font-size="3">Total Fat 11g</text>
    <text class="nutrition-row" x="691" y="853" font-size="3" text-anchor="end">17%</text>
    <text class="nutrition-row" x="616" y="857" font-size="3">Saturated Fat 3g</text>
    <text class="nutrition-row" x="691" y="857" font-size="3" text-anchor="end">15%</text>
    <text class="nutrition-row" x="616" y="861" font-size="3">Trans Fat 0g</text>
    <text class="nutrition-row bold" x="613" y="867" font-size="3">Cholesterol 65mg</text>
    <text class="nutrition-row" x="691" y="867" font-size="3" text-anchor="end">22%</text>
    <text class="nutrition-row bold" x="613" y="872" font-size="3">Sodium 520mg</text>
    <text class="nutrition-row" x="691" y="872" font-size="3" text-anchor="end">24%</text>
    <text class="nutrition-row bold" x="613" y="877" font-size="3">Potassium 44mg</text>
    <text class="nutrition-row" x="691" y="877" font-size="3" text-anchor="end">1%</text>
    <text class="nutrition-row bold" x="613" y="882" font-size="3">Total Carbohydrate 0g</text>
    <text class="nutrition-row" x="691" y="882" font-size="3" text-anchor="end">0%</text>
    <line x1="612" y1="889" x2="692" y2="889" stroke="var(--ink)" stroke-width="0.6"/>
    <text class="nutrition-row bold" x="613" y="894" font-size="3">Protein 14g</text>
  </g>

  <text class="net-weight" x="722" y="839" font-size="27">700g</text>

  <g class="recycle-icon" transform="translate(740,868)">
    <circle r="10" fill="none" stroke="var(--eco-green)" stroke-width="3" stroke-dasharray="14 7"/>
    <path d="M4,-12 L9,-8 L3,-6 Z" fill="var(--eco-green)"/>
    <path d="M-11,5 L-9,11 L-5,5 Z" fill="var(--eco-green)"/>
    <path d="M10,6 L4,11 L6,4 Z" fill="var(--eco-green)"/>
  </g>
</svg>
</body>
</html>
```